Lanternfield Disability - Social Security Disability Attorneys

Our company is expanding to attract clients nationwide for our social security disability practice. We have a logo, but I am looking for a creative and elegant letterhead that projects an image of being technologically advanced but still professional enough for the legal field. I am looking for the "wow factor" combined with this is still professional enough for a law practice.

Requesting letterhead and business card design
Updates

Had to update and change the logo. The previous logo had a typo. Please send updates with the new logo for consideration. The letterhead and business cards should be professional enough to be used for a law firm. Thanks.

Industry/Entity Type

Law Practice, Law Firm, Healthcare Industry, Government

Colors

Designer to choose colors to be used in the design.

Requirements
Nice to have
• **Please create a vertical design for the business card**

```html
<!DOCTYPE html>
<html lang="en">
<head>
<meta charset="utf-8">
<title>Lanternfield Disability – Business Card</title>
<link href="https://fonts.googleapis.com/css2?family=Cinzel:wght@400;600;700&family=Raleway:wght@400;500&display=swap" rel="stylesheet">
<style>
  :root {
    --page-bg: #2b2b2d;
    --brand-blue: #3d66d9;
    --brand-blue-deep: #2f54c4;
    --accent-orange: #ea7a24;
    --card-white: #f6f6f6;
    --ink: #2f2f33;
    --on-blue: #ffffff;
  }
  * { box-sizing: border-box; margin: 0; padding: 0; }
  html, body { width: 1200px; height: 874px; overflow: hidden; }
  body {
    background: var(--page-bg);
    display: flex;
    flex-direction: column;
    align-items: center;
    justify-content: center;
    gap: 32px;
    font-family: "Raleway", sans-serif;
  }
  .card {
    position: relative;
    width: 680px;
    height: 389px;
    border-radius: 22px;
    overflow: hidden;
  }

  /* Back side */
  .card-back {
    background: linear-gradient(160deg, #4670e0 0%, var(--brand-blue) 50%, var(--brand-blue-deep) 100%);
    color: var(--on-blue);
    display: flex;
    flex-direction: column;
    align-items: center;
    justify-content: center;
  }
  .back-brand {
    display: flex;
    align-items: center;
    gap: 14px;
    margin-top: 10px;
  }
  .back-brand .mark-dot {
    width: 22px; height: 22px; border-radius: 50%;
    background: #8fb0ff;
  }
  .back-brand .brand-name {
    font-family: "Cinzel", serif;
    font-weight: 600;
    font-size: 36px;
    letter-spacing: 3px;
    color: #a9c2ff;
  }
  .back-web {
    position: absolute;
    bottom: 62px;
    left: 0; right: 0;
    text-align: center;
    font-size: 15px;
    letter-spacing: 3.5px;
    color: var(--on-blue);
  }

  /* Front side */
  .card-front { background: var(--card-white); }
  .card-front .swoosh { position: absolute; inset: 0; width: 100%; height: 100%; }
  .front-brand {
    position: absolute;
    top: 44px;
    left: 58px;
  }
  .front-brand .brand-row { display: flex; align-items: center; gap: 10px; }
  .front-brand .mark-dot {
    width: 14px; height: 14px; border-radius: 50%;
    background: var(--accent-orange);
  }
  .front-brand .brand-name {
    font-family: "Cinzel", serif;
    font-weight: 600;
    font-size: 27px;
    letter-spacing: 2px;
    color: var(--brand-blue);
  }
  .front-brand .tagline {
    font-family: "Cinzel", serif;
    font-size: 8.5px;
    letter-spacing: 2.6px;
    color: var(--brand-blue);
    margin-top: 2px;
    margin-left: 26px;
    text-transform: uppercase;
  }
  .contact {
    position: absolute;
    top: 150px;
    left: 58px;
    font-size: 14px;
    line-height: 1.38;
    color: var(--ink);
    list-style: none;
  }
  .contact li { display: flex; align-items: center; gap: 9px; }
  .contact .address-block { margin-bottom: 2px; }
  .contact svg { width: 13px; height: 13px; flex: none; fill: var(--brand-blue); }
  .holder {
    position: absolute;
    right: 44px;
    bottom: 30px;
    text-align right;
    text-align: right;
    color: var(--on-blue);
  }
  .holder .name {
    font-family: "Cinzel", serif;
    font-weight: 700;
    font-size: 21px;
    letter-spacing: 0.5px;
    white-space: nowrap;
  }
  .holder .title {
    font-size: 15px;
    letter-spacing: 0.5px;
    margin-top: 2px;
  }
</style>
</head>
<body>

  <section class="card card-back" aria-label="Business card, back">
    <div class="back-brand">
      <span class="mark-dot"></span>
      <span class="brand-name">Lanternfield Disability</span>
    </div>
    <p class="back-web">www.LanternfieldDisability.com</p>
  </section>

  <section class="card card-front" aria-label="Business card, front">
    <svg class="swoosh" viewBox="0 0 680 389" preserveAspectRatio="none" aria-hidden="true">
      <path d="M230 389 Q460 330 640 0 L680 0 L680 389 Z" fill="var(--brand-blue)"/>
      <path d="M175 389 Q405 340 615 35 Q425 335 225 389 Z" fill="var(--accent-orange)"/>
    </svg>

    <div class="front-brand">
      <div class="brand-row">
        <span class="mark-dot"></span>
        <span class="brand-name">Lanternfield Disability</span>
      </div>
      <p class="tagline">Social Security Disability Attorneys</p>
    </div>

    <ul class="contact">
      <li class="address-block">4216 Birchwood Court<br>Juneau, Alaska 99801</li>
      <li>
        <svg viewBox="0 0 24 24"><path d="M6.6 10.8a15.1 15.1 0 0 0 6.6 6.6l2.2-2.2c.3-.3.7-.4 1-.2 1.1.4 2.3.6 3.6.6.6 0 1 .4 1 1V20c0 .6-.4 1-1 1C10.6 21 3 13.4 3 4c0-.6.4-1 1-1h3.5c.6 0 1 .4 1 1 0 1.3.2 2.5.6 3.6.1.3 0 .7-.2 1z"/></svg>
        555-213-4780
      </li>
      <li>
        <svg viewBox="0 0 24 24"><path d="M7 2h10a2 2 0 0 1 2 2v16a2 2 0 0 1-2 2H7a2 2 0 0 1-2-2V4a2 2 0 0 1 2-2zm0 3v13h10V5z"/></svg>
        555-302-6619
      </li>
      <li>
        <svg viewBox="0 0 24 24"><path d="M2 5h20v14H2zm2 2v.5l8 5 8-5V7zm0 2.9V17h16V9.9l-8 5z"/></svg>
        info@lanternfielddisability.com
      </li>
      <li>
        <svg viewBox="0 0 24 24"><path d="M12 2a10 10 0 1 0 0 20 10 10 0 0 0 0-20zm6.9 6h-3a15 15 0 0 0-1.3-3.9A8 8 0 0 1 18.9 8zM12 4c.8 1.2 1.5 2.5 1.9 4h-3.8c.4-1.5 1.1-2.8 1.9-4zM4.3 14a8 8 0 0 1 0-4h3.4a16 16 0 0 0 0 4zm.8 2h3a15 15 0 0 0 1.3 3.9A8 8 0 0 1 5.1 16zm3-8h-3a8 8 0 0 1 4.3-3.9A15 15 0 0 0 8.1 8zM12 20c-.8-1.2-1.5-2.5-1.9-4h3.8c-.4 1.5-1.1 2.8-1.9 4zm2.3-6H9.7a14 14 0 0 1 0-4h4.6a14 14 0 0 1 0 4zm.3 5.9a15 15 0 0 0 1.3-3.9h3a8 8 0 0 1-4.3 3.9zm1.7-5.9a16 16 0 0 0 0-4h3.4a8 8 0 0 1 0 4z"/></svg>
        www.lanternfielddisability.com
      </li>
    </ul>

    <div class="holder">
      <p class="name">DANIEL WHITMORE</p>
      <p class="title">Founder &amp; CEO</p>
    </div>
  </section>

</body>
</html>
```